Professional Home Buyer business card needed

I need a pretty straight forward business card designed. We help people that NEED to sell their homes solve problems. We perform all types of Real Estate transactions including flip, wholesale, investment, rental property and multi family. The card will mainly be used to give to prospective Sellers but will also be given to Real Estate Investors as well. It should professional and very easy to read, most clients are older people.

Target Market(s)

Distressed home sellers as well as Real Estate investors

Industry/Entity Type

Real Estate

Contact Information for Business Card

should be a professional layout

Colors
ec1f27
ffffff
000000

Requirements
Must have
• Large logo on back and smaller one on front. should utilize Red, white, and black.
• I am thinking of using a soft touch coating on the card so keep that in mind.
• Contact info should be very easy to read, think older clients.
Nice to have
• I would like to see a design with rounded corners on the card
Should not have
• pictures of homes or other home graphics.

```html
<!DOCTYPE html>
<html lang="en">
<head>
<meta charset="utf-8">
<title>Keystone Home Buyers – Business Card</title>
<link href="https://fonts.googleapis.com/css2?family=Archivo+Black&family=Arimo:wght@400;700&display=swap" rel="stylesheet">
<style>
  :root {
    --red: #ec1f27;
    --white: #ffffff;
    --black: #000000;
    --ink: #0b0b0b;
    --stage: #222222;
  }
  * { box-sizing: border-box; margin: 0; padding: 0; }
  html, body { width: 1200px; height: 1200px; overflow: hidden; }
  body {
    background: var(--stage);
    font-family: "Arimo", Arial, sans-serif;
    position: relative;
  }
  .card {
    position: absolute;
    left: 150px;
    width: 900px;
    height: 514px;
    border-radius: 28px;
    overflow: hidden;
  }
  .card--back { top: 66px; background: var(--ink); }
  .card--front { top: 620px; background: var(--white); }

  .brand {
    position: absolute;
    left: 0; right: 0;
    display: flex;
    flex-direction: column;
    align-items: center;
    font-family: "Archivo Black", Arial, sans-serif;
    text-transform: uppercase;
    line-height: 1;
  }
  .brand__row { display: flex; align-items: center; gap: 18px; }
  .brand__mark { width: 30px; height: 30px; background: var(--red); }
  .brand__name { letter-spacing: 2px; }
  .brand__sub { letter-spacing: 12px; margin-top: 16px; padding-left: 12px; }

  .card--back .brand { top: 185px; color: var(--white); }
  .card--back .brand__name { font-size: 78px; }
  .card--back .brand__sub { font-size: 30px; }

  .card--front .brand { top: 60px; color: var(--black); }
  .card--front .brand__name { font-size: 60px; }
  .card--front .brand__sub { font-size: 24px; letter-spacing: 10px; margin-top: 12px; }
  .card--front .brand__mark { width: 24px; height: 24px; }

  .contact-band {
    position: absolute;
    left: 0; right: 0;
    top: 240px; height: 236px;
    background: var(--black);
    color: var(--white);
  }
  .stripe-gap { position: absolute; left: 0; right: 0; top: 476px; height: 6px; background: var(--white); }
  .stripe { position: absolute; left: 0; right: 0; top: 482px; bottom: 0; background: var(--red); }

  .person { text-align: center; margin-top: 30px; }
  .person__name {
    font-family: "Archivo Black", Arial, sans-serif;
    font-size: 34px;
    letter-spacing: 1px;
    text-transform: uppercase;
  }
  .person__title {
    color: var(--red);
    font-size: 26px;
    font-weight: 700;
    letter-spacing: 2px;
    text-transform: uppercase;
    margin-top: 4px;
  }

  .details {
    display: flex;
    justify-content: center;
    align-items: center;
    margin-top: 28px;
    gap: 28px;
    font-size: 23px;
  }
  .details__col { display: flex; flex-direction: column; gap: 12px; }
  .details__col--left { align-items: flex-end; }
  .details__divider { width: 2px; height: 74px; background: #7a7a7a; }
  .detail { display: flex; align-items: center; gap: 12px; white-space: nowrap; }
  .icon { width: 22px; height: 22px; flex: none; }
</style>
</head>
<body>

  <section class="card card--back" aria-label="Card back">
    <div class="brand">
      <div class="brand__row">
        <span class="brand__name">Keystone</span>
        <span class="brand__mark"></span>
      </div>
      <span class="brand__sub">Home Buyers</span>
    </div>
  </section>

  <section class="card card--front" aria-label="Card front">
    <div class="brand">
      <div class="brand__row">
        <span class="brand__name">Keystone</span>
        <span class="brand__mark"></span>
      </div>
      <span class="brand__sub">Home Buyers</span>
    </div>

    <div class="contact-band">
      <div class="person">
        <div class="person__name">Daniel Marsh</div>
        <div class="person__title">President</div>
      </div>

      <div class="details">
        <div class="details__col details__col--left">
          <div class="detail">
            <span>555-014-2276</span>
            <svg class="icon" viewBox="0 0 24 24"><path fill="#ec1f27" d="M6.6 10.8a15.1 15.1 0 0 0 6.6 6.6l2.2-2.2a1 1 0 0 1 1-.25 11.4 11.4 0 0 0 3.6.57 1 1 0 0 1 1 1V20a1 1 0 0 1-1 1A17 17 0 0 1 3 4a1 1 0 0 1 1-1h3.5a1 1 0 0 1 1 1c0 1.25.2 2.45.57 3.57a1 1 0 0 1-.25 1z"/></svg>
          </div>
          <div class="detail">
            <span>daniel@plainshomeoffers.com</span>
            <svg class="icon" viewBox="0 0 24 24"><rect x="2" y="5" width="20" height="14" fill="#ec1f27"/><path d="M2 5l10 8 10-8" fill="none" stroke="#000" stroke-width="1.8"/></svg>
          </div>
        </div>

        <span class="details__divider"></span>

        <div class="details__col">
          <div class="detail">
            <svg class="icon" viewBox="0 0 24 24"><path fill="#ec1f27" d="M12 2a7 7 0 0 0-7 7c0 5.2 7 13 7 13s7-7.8 7-13a7 7 0 0 0-7-7zm0 9.5A2.5 2.5 0 1 1 12 6.5a2.5 2.5 0 0 1 0 5z"/></svg>
            <span>P.O. Box 118, Fairview, KS 67000</span>
          </div>
          <div class="detail">
            <svg class="icon" viewBox="0 0 24 24"><g fill="none" stroke="#ec1f27" stroke-width="2"><circle cx="12" cy="12" r="9.5"/><ellipse cx="12" cy="12" rx="4" ry="9.5"/><path d="M2.5 12h19M4 7h16M4 17h16"/></g></svg>
            <span>www.plainshomeoffers.com</span>
          </div>
        </div>
      </div>
    </div>
    <div class="stripe-gap"></div>
    <div class="stripe"></div>
  </section>

</body>
</html>
```